DWR Logistics Marketing flyer

Good morning, I run a trucking company and I will be needing help setting up a website logo and a marketing flyer or something like that talking about our services and what we can offer to potential new customers who need to ship their product. I need help getting this all together.

Target Market(s)

Transportation customers

Requirements
Must have
• should list our services and contact info
Nice to have
• the Logo on the top

```html
<!DOCTYPE html>
<html lang="en">
<head>
<meta charset="utf-8">
<title>DWR Logistics Flyer</title>
<link rel="stylesheet" href="https://fonts.googleapis.com/css2?family=Michroma&family=Lato:wght@400;700&display=swap">
<style>
:root{
  --navy:#150a2e;
  --orange:#f7860f;
  --white:#ffffff;
  --ink:#1a1a1a;
  --stage:#666666;
}
*{margin:0;padding:0;box-sizing:border-box}
html,body{width:1200px;height:853px;overflow:hidden;background:var(--stage)}
body{position:relative;font-family:"Lato",sans-serif;color:var(--ink)}
.page{position:absolute;top:42px;width:547px;height:772px;overflow:hidden}
.page--front{left:34px;background:var(--navy)}
.page--back{left:619px;background:var(--white)}
.abs{position:absolute}
.heading{font-family:"Michroma",sans-serif;text-transform:uppercase;letter-spacing:.02em;white-space:nowrap}
.brand{font-family:"Michroma",sans-serif;font-size:13px;white-space:nowrap;display:flex;align-items:center;gap:6px}
.brand-mark{width:10px;height:10px;display:inline-block}
.photo{position:absolute;overflow:hidden}
.circle{border-radius:50%;border:4px solid var(--orange)}
.body-text{font-size:9px;white-space:nowrap}
.contact{color:var(--orange);font-size:13.5px;white-space:nowrap;display:flex;align-items:center;gap:5px}
.contact svg{width:10px;height:10px;fill:var(--orange)}
/* front */
.hero-fade{left:100px;top:0;width:280px;height:130px;background:linear-gradient(180deg,#c9c3d8 0%,#e7e3ef 50%,rgba(255,255,255,0) 100%)}
.front-brand{right:28px;top:56px;color:var(--navy)}
.front-brand .brand-mark{background:var(--orange)}
.welcome{right:28px;top:96px;font-size:14px;color:var(--navy)}
.tagline{right:28px;top:125px;width:430px;text-align:right;color:var(--orange);font-weight:700;font-size:12.4px;line-height:23px}
.about-title{right:62px;top:209px;font-size:12px;color:var(--navy)}
.about-text{right:28px;top:230px;text-align:right;line-height:20.2px}
.offer-title{left:27px;top:567px;font-size:13px;color:var(--white)}
.offer-text{left:27px;top:590px;width:495px;color:var(--white);line-height:22px;white-space:normal}
.front-contact{top:737px}
/* back */
.services-title{left:28px;top:17px;font-size:12.6px;color:var(--navy)}
.services-text{left:28px;top:39px;line-height:20.2px}
.frame{top:111px;width:157px;height:119px;border:1px solid var(--orange);background:var(--white);box-shadow:0 0 4px rgba(0,0,0,.12)}
.frame .photo{left:6px;top:5px;right:6px;bottom:5px}
.caption{top:245px;width:157px;text-align:center;font-family:"Michroma",sans-serif;font-size:8.5px;color:var(--ink)}
.more-text{left:28px;top:273px;line-height:22px}
.award-text{left:28px;top:361px;line-height:22px}
.contact-title{left:28px;top:676px;font-size:12.7px;color:var(--white)}
.back-brand{right:28px;top:668px;color:var(--white);font-size:13px}
.back-brand .brand-mark{background:var(--orange)}
</style>
</head>
<body>

<section class="page page--front">
  <svg class="abs" width="547" height="772" viewBox="0 0 547 772" style="left:0;top:0">
    <path d="M108,0 C30,70 25,300 150,440 C240,540 420,565 547,528 L547,0 Z" fill="var(--orange)"/>
    <path d="M122,0 C55,75 55,290 165,420 C250,520 420,545 547,516 L547,0 Z" fill="var(--white)"/>
  </svg>
  <div class="abs hero-fade" role="img" aria-label="Row of white semi trucks parked in a line"></div>

  <div class="abs brand front-brand"><span class="brand-mark"></span>DWR LOGISTICS</div>
  <h1 class="abs heading welcome">Welcome to DWR Logistics</h1>
  <p class="abs tagline">We are a transportation company that specializes in logistics to maximize efficiency in gettingthe product from shipper to customer in the shortest safest time possible</p>

  <h2 class="abs heading about-title">About DWR Logistics</h2>
  <p class="abs body-text about-text">We have the knowledge and ability to handle any dry van, Reefer, flatbed, or tanker load that<br>needs to be moved, and strive to be your number one call to bring or move<br>any product that your company may need. With our current 30 truck fleet<br>We can service customers locally to across country with solo and team drivers to<br>make sure that your product is to your customers in the time frame promised.<br>We also can adjust to each customers needs so If the need arises,<br>we can add to the fleet to make sure that you the customer are getting the<br>service that you need. We work through the problems<br>to find the right solution then get it executed quickly and effectively.<br>You are not just another number to us you are what makes our company<br>possible, and we value that relationship.</p>

  <div class="photo circle" style="left:29px;top:273px;width:178px;height:178px;background:radial-gradient(circle at 40% 35%,#f6d27a,#d98a3a 45%,#6f7a3c 80%)" role="img" aria-label="Two trucks driving on a country highway at sunset"></div>
  <div class="photo circle" style="left:207px;top:433px;width:142px;height:142px;background:linear-gradient(135deg,#8a8f99,#b8632c 50%,#7a5638)" role="img" aria-label="Workers loading boxes into a truck at a warehouse dock"></div>
  <div class="photo circle" style="left:415px;top:475px;width:102px;height:102px;background:linear-gradient(160deg,#6b5d52,#c9a27a 55%,#8c4b3a)" role="img" aria-label="Warehouse interior with stacked pallets"></div>

  <h2 class="abs heading offer-title">What can we offer</h2>
  <p class="abs body-text offer-text">Nam libero tempore, cum soluta nobis est eligendi optio cumque nihil impedit quo minus id quod maxime placeat facere orrupti quos dolores et quas molestias excepturi sint occaecati cupiditate non provident, bus maiores alias consequatur aut perferendis dosimilique sunt in culpa qui officia deserunt mollitia animi, id est laborum et dolorum fuga.Temporibus autem quibusdam et aut officiis debitis aut rerum necessitatibus saepe eveniet ut et voluptates repudiandae sint et molestiae non recusandae. Itaque earum rerum hic tenetur a sapiente delectus, ut aut reiciendis voluptatibus maiores alias consequatur aut perferendis doloribus asperiores repellat.</p>

  <div class="abs contact front-contact" style="left:27px"><svg viewBox="0 0 10 10"><path d="M5,0 C2.5,0 1,1.8 1,3.8 C1,6.5 5,10 5,10 C5,10 9,6.5 9,3.8 C9,1.8 7.5,0 5,0 Z M5,5.3 A1.5,1.5 0 1 1 5,2.3 A1.5,1.5 0 1 1 5,5.3 Z"/></svg>Location: 418 Oak Ct. Merrowfield, IN. 47000</div>
  <div class="abs contact front-contact" style="left:315px"><svg viewBox="0 0 10 10"><path d="M0,2 L10,2 L10,8.5 L0,8.5 Z" /><path d="M0,2.3 L5,5.6 L10,2.3" stroke="var(--navy)" stroke-width="1" fill="none"/></svg>&nbsp;Mail: dwrlogisticsllc@mailpost.com</div>
</section>

<section class="page page--back">
  <h2 class="abs heading services-title">Our Services</h2>
  <p class="abs body-text services-text">We take pride in our work and our customer service from pick up to delivery. Our current customer list handles more than<br>half of the nation’s orange Juice, hauling the corn oil that fries the potatoes chips for the one of the nations largest potato<br>chip suppliers, to hauling wine from the west coast doing plant to plant transfers to the plants on the east coast.</p>

  <div class="abs frame" style="left:28px"><div class="photo" style="background:linear-gradient(180deg,#9fb4c8,#c46a4a 55%,#5a5f66)" role="img" aria-label="Red truck with shipping container on a wet road"></div></div>
  <div class="abs frame" style="left:195px"><div class="photo" style="background:linear-gradient(160deg,#d8c9a8,#8d8f94 50%,#4e5258)" role="img" aria-label="Aerial view of trailers at a distribution center loading docks"></div></div>
  <div class="abs frame" style="left:362px"><div class="photo" style="background:linear-gradient(180deg,#6fa6c9,#d9c49a 55%,#7a6a4c)" role="img" aria-label="Trucks on a highway with a digital network overlay"></div></div>
  <div class="abs caption" style="left:28px">ITAQUE EARUM</div>
  <div class="abs caption" style="left:195px">ITAQUE EARUM</div>
  <div class="abs caption" style="left:362px">ITAQUE EARUM</div>

  <p class="abs body-text more-text">We also branch out to haul the corn syrup in to make the wine and alcohol out of the plant in the Midwest to the different<br>plants that make alcohol. In short, from a transportation standpoint if you need it, we can bring it to you rather it is the<br>ingredient’s coming in to your plant or your product leaving.</p>

  <p class="abs body-text award-text">To date we have won the Northline carrier excellence award two years in a row servicing their major customers across the<br>different brokerage networks along with we are the number one truck supplier to two of the major orange juice<br>manufacturers in the US for when they bring their product into port side in Florida, and it needs to go to their<br>manufacturing facility throughout the state. In the past year we have hauled over 40 million gallons of orange juice,<br>another million gallons of wine and alcohol and millions of gallons of corn oil to service the nation’s food industry with the<br>ability to add to that ever-growing number. What sets us apart from any other carrier is that when you call you will get<br>either the owner or the individual that makes as many decisions as possible, you will not have to wait for approvals and<br>time wasted. We work through the problems to find the right solution then get it executed quickly and effectively. You are<br>not just another number to us you are what makes our company possible, and we value that relationship.<br>Our references include those from<br>Bellavista citrus products, Sunmere juice north America, Crispfield snacks, and Harbor Spirits.</p>

  <svg class="abs" width="547" height="772" viewBox="0 0 547 772" style="left:0;top:0">
    <path d="M547,533 C470,610 300,650 0,636 L0,772 L547,772 Z" fill="var(--orange)"/>
    <path d="M547,552 C470,625 300,660 0,645 L0,772 L547,772 Z" fill="var(--navy)"/>
  </svg>

  <h2 class="abs heading contact-title">Contact us</h2>
  <div class="abs brand back-brand"><span class="brand-mark"></span>DWR LOGISTICS</div>
  <div class="abs contact" style="left:28px;top:712px"><svg viewBox="0 0 10 10"><path d="M5,0 C2.5,0 1,1.8 1,3.8 C1,6.5 5,10 5,10 C5,10 9,6.5 9,3.8 C9,1.8 7.5,0 5,0 Z M5,5.3 A1.5,1.5 0 1 1 5,2.3 A1.5,1.5 0 1 1 5,5.3 Z"/></svg>Location: 418 Oak Ct. Merrowfield, IN. 47000</div>
  <div class="abs contact" style="left:316px;top:711px"><svg viewBox="0 0 10 10"><path d="M0,2 L10,2 L10,8.5 L0,8.5 Z"/><path d="M0,2.3 L5,5.6 L10,2.3" stroke="var(--navy)" stroke-width="1" fill="none"/></svg>&nbsp;Mail: dwrlogisticsllc@mailpost.com</div>
  <div class="abs contact" style="left:28px;top:742px"><svg viewBox="0 0 10 10"><path d="M2,0.5 L3.8,0.5 L4.5,3 L3.3,4 C3.9,5.4 4.8,6.3 6.1,6.9 L7.1,5.7 L9.5,6.4 L9.5,8.2 C9.5,9 8.8,9.6 8,9.5 C4.2,9 1,5.8 0.5,2 C0.4,1.2 1.1,0.5 2,0.5 Z"/></svg>Call: 555-014-2738</div>
</section>

</body>
</html>
```